CupMarketry

-
Below info still applicable but I wanted to highlight the point that I am looking for a design similar to the style loopnest with the mentioned color scheme (below). If you do that then the project is yours, I'm happy with an almost clone design. I know this is a completely different type of app but what I mean is:
- The listings to look like the loopnest widgets (i.e. blocks, three column, and clearly seperated)
- Adverts and listings mixed together in the results set
- Prominent listings to take up 2 or 3 of the columns instead, non prominent ones to take up 1.
- Clear spacing between the listings, as with loopnest widgets
- Clear seperation between menu and widgets as with loopnest
- Search/filters and category filters on the right or left, as with loopnest
Again, if this is not clear I want it LIKE LOOPNEST, so far had stock template designs that weren't anything like this.
Loopnest is not the only site I listed for inspiration, but I think its easier at this point to just say clone the damn thing, and re purpose it for coffee. We will make additional changes at development time to make it distinct and incorporate some of the other things we were looking for.
-
Hi All,
I'm looking to get designs for a new site that allows coffee roasters, and barista equipment suppliers to sell their goods to coffee shops via an auction site. So essentially B2B bidora targeted at the coffee market.
Pages required:
All pages:
- Logo
- Login/register links (or my account if logged in)
- links to Contact us, FAQs, Advertise with us
Homepage:
- Search bar
- List of filter categories
- Latest products section
- Advertising section
Search page:
- Listings (Image, price (buy now or current bid), postage price, no bids, time remaining to bid)
- Advertising
Listing page
- Same listing info as above but with full description, multipule images to select from, time ending and and a bid form (enter amount) or buy now button.
Login page
- Username/Password
- Alternative login via Chatterly
My account:
- Link to add listings
- List of current listings
- List of current bids
- Link to purchase history
Add a listing:
- Form page to add a listing
- Requires
- Images uploads (drag to upload, as well as normal)
- Title field
- Description field
- Amount field
- Quantity field
- Postage amount field
- Category Drop down field
- End date/time picker field
That's it for functionality, with regards to design this needs to be designed in a way that is compatible with framekit components (http://quillbird.codehost.example/framekit/), though framekit is highly customizable so don't feel too restricted.
Styles/colours:
Site layout should be clean, and clear utilizing white space well i.e.
- http://lnk.example/qrTwp
- http://lnk.example/VbHsd
- https://loopnest.example/
Also VERY much like the vantrix "tessera" style design i.e. square boxes. If you know what I mean by this then cool, if not don't worry about it.
The logo on the other hand should have and earthy, organic feel to it.
Also, please only use fonts available from typevault (http://www.typevault.example/faces/).

```html
<!DOCTYPE html>
<html lang="en">
<head>
<meta charset="utf-8">
<title>CupMarketry – Listing</title>
<link href="https://fonts.googleapis.com/css2?family=Arimo:ital,wght@0,400;0,700;1,400&display=swap" rel="stylesheet">
<style>
:root{
  --brown:#9a5a37;
  --brown-dark:#6b3518;
  --brown-btn:#a85f3d;
  --blue:#3a7fcf;
  --red:#d83344;
  --green:#2e9b2e;
  --ink:#333;
  --muted:#555;
  --band:#f3f3f3;
  --line:#d6d6d6;
  --footer:#e9e9e9;
}
*{box-sizing:border-box;margin:0;padding:0}
html,body{width:1200px;height:1089px;overflow:hidden}
body{position:relative;background:#fff;font-family:"Arimo",Arial,sans-serif;color:var(--ink)}
.abs{position:absolute}
.site-header{left:0;top:0;width:1200px;height:108px;background:var(--band);box-shadow:0 3px 4px rgba(0,0,0,.18)}
.brand-mark{left:14px;top:11px;width:80px;height:80px;border-radius:50%;background:var(--brown)}
.brand-name{left:104px;top:33px;font-size:31px;color:var(--brown);font-weight:400;letter-spacing:-.5px}
.top-links{right:14px;top:9px;display:flex;font-size:14px;color:#444}
.top-links span{padding:0 18px;border-left:1px solid #bbb;line-height:17px}
.top-links span:first-child{border-left:0}
.top-links span:last-child{padding-right:0}
.btn{display:flex;align-items:center;justify-content:center;color:#fff;font-weight:700;border-radius:4px}
.btn-login{left:884px;top:53px;width:126px;height:41px;background:var(--brown-btn);font-size:17px;box-shadow:0 2px 2px rgba(0,0,0,.25)}
.btn-register{left:1034px;top:53px;width:149px;height:41px;background:var(--blue);font-size:17px;box-shadow:0 2px 2px rgba(0,0,0,.25)}
.search-input{left:28px;top:147px;width:317px;height:31px;border:1px solid #ccc;border-radius:3px;background:#fff}
.search-btn{left:351px;top:147px;width:91px;height:31px;background:var(--brown-btn);font-size:14px;font-weight:400;border-radius:2px}
.back-btn{left:926px;top:141px;width:267px;height:42px;border:1px solid #ccc;border-radius:3px;background:linear-gradient(#fafafa,#e4e4e4);display:flex;align-items:center;gap:10px;padding-left:14px;font-size:16px;font-weight:700;color:#444}
.featured{left:0;top:206px;width:1200px;height:284px;background:var(--band)}
.featured-title{left:18px;top:241px;font-size:26px;line-height:31px;color:var(--brown)}
.featured-brand{left:24px;top:332px;font-size:19px;color:#111}
.tile{width:205px;top:225px;text-align:center}
.tile .photo{height:219px;border:3px solid #ddd;border-radius:3px}
.tile .name{font-size:13px;color:#555;margin-top:9px}
.tile .price{font-size:13px;color:var(--brown);margin-top:3px}
.pointer{left:320px;top:483px}
.shadow-line{left:300px;top:490px;width:900px;height:4px;background:linear-gradient(90deg,rgba(0,0,0,0),rgba(0,0,0,.25),rgba(0,0,0,0))}
.gallery{left:19px;top:512px;width:507px;height:474px;border:1px solid var(--line);border-radius:3px;background:#f8f8f8}
.main-photo{left:28px;top:519px;width:490px;height:306px;background:radial-gradient(circle at 55% 45%,#8a5a3a,#3a1f10 70%,#2a150a)}
.thumb{top:840px;width:138px;height:130px;background:radial-gradient(circle at 60% 40%,#8a5a3a,#3a1f10 75%)}
.arrow{top:882px;font-size:36px;color:#c8c8c8}
.info{left:537px;width:620px}
.h-product{top:521px;font-size:21px;color:var(--brown)}
.p{font-size:13px;line-height:15px;color:var(--muted)}
.h-roast{top:586px;font-size:21px;font-style:italic;color:var(--brown-dark)}
.roast-text{top:616px;color:var(--brown-dark)}
.h-sec{font-size:18px;color:var(--brown-dark)}
.bid-form{left:975px;top:678px;width:208px;height:308px;border:1px solid var(--line);border-radius:3px;background:#f6f6f6}
.bid-form .h{position:absolute;left:17px;top:12px;font-size:18px;color:#666}
.bid-amount{position:absolute;left:15px;top:45px;width:178px;height:78px;background:#fff;border:1px solid #ddd;display:flex;align-items:center;justify-content:center;font-size:35px;color:#333}
.bid-row{position:absolute;left:19px;font-size:13px;color:#444}
.timer{position:absolute;left:19px;top:172px;width:168px;height:32px;background:#f7c9c9;display:flex;align-items:center;justify-content:center;font-size:18px;color:#444}
.bid-input{position:absolute;left:19px;top:216px;width:108px;height:28px;background:#fff;border:1px solid #ccc;font-size:13px;color:#555;display:flex;align-items:center;justify-content:center}
.bid-btn{position:absolute;left:133px;top:216px;width:54px;height:28px;background:var(--blue);border-radius:3px;font-size:14px;font-weight:400}
.buy-btn{position:absolute;left:19px;top:255px;width:168px;height:36px;background:linear-gradient(#e84556,#cf2a3b);border-radius:3px;font-size:19px;font-weight:400}
.footer{left:0;top:1025px;width:1200px;height:64px;background:var(--footer);font-size:14px;color:#444}
.footer span{position:absolute;top:21px}
</style>
</head>
<body>
<header class="abs site-header"></header>
<div class="abs brand-mark"></div>
<div class="abs brand-name">CupMarketry</div>
<nav class="abs top-links"><span>Contact us</span><span>FAQ</span><span>Advertise with us</span></nav>
<div class="abs btn btn-login">Login</div>
<div class="abs btn btn-register">Register</div>

<div class="abs search-input"></div>
<div class="abs btn search-btn">Search</div>
<div class="abs back-btn">
  <svg width="26" height="24" viewBox="0 0 26 24"><path d="M10 3 L2 10 L10 17 V12 C17 12 21 14 24 21 C23 12 18 8 10 8 Z" fill="#444"/></svg>
  Back to previous search
</div>

<section class="abs featured"></section>
<div class="abs featured-title">Product Name<br>Goes Here</div>
<div class="abs featured-brand">Industry / Brand</div>
<div class="abs tile" style="left:230px"><div class="photo" role="img" aria-label="Roasted coffee beans in a burlap sack" style="background:radial-gradient(circle at 50% 40%,#7a4a2a,#3a1f10 75%)"></div><div class="name">Product Name</div><div class="price">120$</div></div>
<div class="abs tile" style="left:479px"><div class="photo" role="img" aria-label="Espresso cup on a saucer surrounded by beans" style="background:radial-gradient(circle at 50% 40%,#e8e2da,#6a4128 60%,#3a2214)"></div><div class="name">Product Name</div><div class="price">120$</div></div>
<div class="abs tile" style="left:715px"><div class="photo" role="img" aria-label="Steaming coffee cup with beans on a dark table" style="background:radial-gradient(circle at 35% 60%,#b58a62,#5a2e14 55%,#2a1206)"></div><div class="name">Product Name</div><div class="price">120$</div></div>
<div class="abs tile" style="left:945px"><div class="photo" role="img" aria-label="Metal scoops in sacks of coffee beans" style="background:radial-gradient(circle at 50% 40%,#8a6a50,#3a1f10 70%)"></div><div class="name">Product Name</div><div class="price">120$</div></div>
<svg class="abs pointer" width="18" height="9" viewBox="0 0 18 9"><path d="M0 9 L9 0 L18 9 Z" fill="#fff"/></svg>
<div class="abs shadow-line"></div>

<div class="abs gallery"></div>
<div class="abs main-photo" role="img" aria-label="Metal scoop resting in a sack of roasted coffee beans"></div>
<div class="abs thumb" style="left:50px" role="img" aria-label="Coffee beans with scoop, thumbnail"></div>
<div class="abs thumb" style="left:205px" role="img" aria-label="Coffee beans with scoop, thumbnail"></div>
<div class="abs thumb" style="left:353px" role="img" aria-label="Coffee beans with scoop, thumbnail"></div>
<div class="abs arrow" style="left:27px">&#10094;</div>
<div class="abs arrow" style="left:499px">&#10095;</div>

<div class="abs info h-product">Product Name goes Here</div>
<p class="abs info p" style="top:549px">Lorem ipsum dolor sit amet, consectetuer adipiscing elit. Aenean commodo ligula eget dolor.</p>
<div class="abs info h-roast">Coffee Roast</div>
<p class="abs info p roast-text">Lorem ipsum dolor sit amet, consectetuer adipiscing elit. Aenean commodo ligula eget dolor. Aenean massa. Cum sociis natoque penatibus et magnis dis parturient montes, nascetur ridiculus mus. Donec quam felis, ultricies nec, pellentesque eu, pretium quis, sem. Nulla consequat</p>
<div class="abs info h-sec" style="top:685px">Availablity</div>
<div class="abs" style="left:542px;top:718px;font-size:15px;color:var(--green)">In Stock</div>
<p class="abs p" style="left:541px;top:744px;width:380px">Product is available in the stock. Product will be delivered up on your purchase</p>
<div class="abs info h-sec" style="top:804px">Description</div>
<p class="abs p" style="left:541px;top:832px;width:420px">Lorem ipsum dolor sit amet, consectetuer adipiscing elit. Aenean commodo ligula eget dolor. Aenean massa. Cum sociis natoque penatibus et magnis dis parturient montes, nascetur ridiculus mus. Donec quam felis, ultricies nec, pellentesque eu, pretium quis, sem. Nulla consequat massa quis enim. Donec pede justo, fringilla vel, aliquet nec, vulputate eget, arcu.</p>

<aside class="abs bid-form">
  <div class="h">Bid Form</div>
  <div class="bid-amount">150 $</div>
  <div class="bid-row" style="top:129px;width:168px;display:flex;justify-content:space-between"><span>Total Bids :</span><span>1250</span></div>
  <div class="bid-row" style="top:150px">Time Remaining to bid</div>
  <div class="timer">12:00:32 Hours</div>
  <div class="bid-input">Enter your bid</div>
  <div class="btn bid-btn">Bid</div>
  <div class="btn buy-btn">Buy Now</div>
</aside>

<footer class="abs footer"><span style="left:18px">© CupMarketry</span><span style="right:16px">All Rights Reserved</span></footer>
</body>
</html>
```